The tide parlor saltwater aquarium store business card

Looking for a serious business card for a saltwater fish and coral store. I want this thing to blow people's minds when they see it. I would like the card to look very professional but I also want people to know what the tide parlor is just by seeing the card. Iam pretty open to anything as long as it's one of a kind.

Industry/Entity Type

Business

Contact Information for Business Card

18735 Calder highway Brookvale pa 16210. Thetideparlor.com. Customerservice@thetideparlor.com. 5038826417

Requirements
Should not have
• Please no child like fish designs

```html
<!DOCTYPE html>
<html lang="en">
<head>
<meta charset="utf-8">
<title>The tide parlor — business card</title>
<link href="https://fonts.googleapis.com/css2?family=Arimo:wght@400;700&display=swap" rel="stylesheet">
<style>
  :root {
    --backdrop: #141414;
    --card-white: #f7f7f7;
    --card-black: #0c0c0c;
    --brand-blue: #3a86c8;
    --band-light: #5fb3e0;
    --band-deep: #2a78c2;
    --ink: #2b2b2b;
    --ink-soft: #444;
    --web-grey: #9aa3ad;
  }
  * { margin: 0; padding: 0; box-sizing: border-box; }
  html, body {
    width: 1200px; height: 864px; overflow: hidden;
    background: var(--backdrop);
    font-family: "Arimo", Arial, sans-serif;
  }
  .stage {
    position: relative; width: 1200px; height: 864px;
    display: flex; align-items: center; justify-content: center; gap: 60px;
  }
  .card {
    position: relative; width: 500px; height: 290px;
    border-radius: 3px; overflow: hidden;
  }
  .card-front { background: var(--card-white); }
  .card-back { background: var(--card-black); }

  .brand {
    display: flex; align-items: center; gap: 8px;
    color: var(--brand-blue); font-weight: 700;
  }
  .brand-dot {
    width: 14px; height: 14px; border-radius: 50%;
    background: var(--brand-blue);
  }
  .card-front .brand { position: absolute; top: 58px; right: 40px; font-size: 22px; }

  .holder { position: absolute; left: 44px; top: 122px; }
  .holder-name { color: var(--brand-blue); font-weight: 700; font-size: 17px; }
  .holder-role { color: var(--ink); font-size: 12px; margin-top: 2px; }

  .contact {
    position: absolute; left: 44px; top: 178px;
    font-size: 12px; color: var(--ink-soft); line-height: 1.4;
  }
  .contact-line { display: flex; align-items: center; gap: 8px; }
  .contact-line svg { width: 12px; height: 12px; fill: var(--band-deep); }
  .contact-address { margin-top: 2px; margin-left: -4px; color: var(--ink); }

  .band {
    position: absolute; left: 0; right: 0; bottom: 0; height: 9px;
    background: linear-gradient(90deg, var(--band-deep), var(--band-light));
  }

  .card-back .brand {
    position: absolute; left: 50%; top: 110px; transform: translateX(-50%);
    font-size: 30px; white-space: nowrap;
  }
  .card-back .brand-dot { width: 18px; height: 18px; }
  .website {
    position: absolute; left: 0; right: 0; top: 196px; text-align: center;
    font-size: 13px; color: var(--web-grey);
  }
</style>
</head>
<body>
<main class="stage">
  <section class="card card-front">
    <div class="brand"><span class="brand-dot"></span><span class="brand-name">The tide parlor</span></div>
    <div class="holder">
      <p class="holder-name">Marcus Hale</p>
      <p class="holder-role">Owner</p>
    </div>
    <div class="contact">
      <p class="contact-line">
        <svg viewBox="0 0 24 24" aria-hidden="true"><path d="M6.6 10.8a15.1 15.1 0 0 0 6.6 6.6l2.2-2.2a1 1 0 0 1 1-.25 11.4 11.4 0 0 0 3.6.57 1 1 0 0 1 1 1V20a1 1 0 0 1-1 1A17 17 0 0 1 3 4a1 1 0 0 1 1-1h3.5a1 1 0 0 1 1 1c0 1.25.2 2.450.57 3.57a1 1 0 0 1-.25 1z"/></svg>
        503-882-6417
      </p>
      <p class="contact-line">
        <svg viewBox="0 0 24 24" aria-hidden="true"><path d="M2 5h20v14H2zm2 2v.5l8 5 8-5V7zm0 3v7h16v-7l-8 5z"/></svg>
        Customerservice@thetideparlor.com
      </p>
      <p class="contact-address">18735 Calder highway,<br>Brookvale pa 16210</p>
    </div>
    <div class="band"></div>
  </section>

  <section class="card card-back">
    <div class="brand"><span class="brand-dot"></span><span class="brand-name">The tide parlor</span></div>
    <p class="website">www.Thetideparlor.com</p>
  </section>
</main>
</body>
</html>
```